we do all sorts of cleaning however bookings are limited!
why not chose the right cleaners for you!
pressure cleaning, window cleaning, office, end of lease clean, accommodation, industrial and commercial cleaning and house cleaning

Logo Text

Bright Nest Cleaning Service

```html
<!DOCTYPE html>
<html lang="en">
<head>
<meta charset="utf-8">
<title>Bright Nest Cleaning Service – Business Cards</title>
<link rel="stylesheet" href="https://fonts.googleapis.com/css2?family=Montserrat:wght@400;500;600;700&display=swap">
<style>
  :root {
    --page-bg: #2b2e33;
    --card-white: #f7f5f6;
    --card-black: #050505;
    --brand-blue: #25a7e0;
    --brand-green: #8cc63f;
    --line-white: #ffffff;
  }
  * { box-sizing: border-box; margin: 0; padding: 0; }
  html, body {
    width: 1200px; height: 1200px; overflow: hidden;
    background: var(--page-bg);
    font-family: "Montserrat", sans-serif;
  }
  .canvas { position: relative; width: 1200px; height: 1200px; }
  .card {
    position: absolute; left: 145px; width: 910px; height: 520px;
    overflow: hidden; border-radius: 4px;
  }
  .card-front { top: 40px; background: var(--card-white); }
  .card-back { top: 640px; background: var(--card-black); }
  .card-wave { position: absolute; inset: 0; width: 100%; height: 100%; }

  .name-block {
    position: absolute; left: 60px; top: 52px;
    border-left: 8px solid var(--brand-green); padding-left: 18px;
    color: var(--brand-blue);
  }
  .person-name { font-size: 32px; font-weight: 600; line-height: 1.1; }
  .person-role { font-size: 24px; font-weight: 500; margin-top: 2px; }
  .address { position: absolute; left: 86px; top: 150px; color: var(--brand-blue); font-size: 21px; line-height: 1.3; }
  .contact-list {
    position: absolute; left: 60px; top: 222px; list-style: none;
    color: var(--brand-blue); font-size: 21px; line-height: 1.35;
  }
  .contact-list li { display: flex; align-items: center; gap: 12px; }
  .contact-icon { width: 14px; height: 14px; flex: none; }

  .brand-mark {
    position: absolute; display: flex; align-items: center; gap: 14px;
    color: var(--brand-blue); font-weight: 700; line-height: 1.05;
  }
  .brand-dot { width: 22px; height: 22px; border-radius: 50%; background: var(--brand-blue); flex: none; }
  .card-front .brand-mark { right: 70px; top: 200px; font-size: 40px; }
  .card-back .brand-mark { right: 60px; top: 50px; font-size: 36px; }
  .brand-sub { display: block; font-size: 0.5em; letter-spacing: 0.08em; margin-top: 6px; }

  .service-list {
    position: absolute; left: 52px; top: 160px; list-style: none;
    color: var(--brand-green); font-size: 19px; font-weight: 500;
    letter-spacing: 0.02em; line-height: 1.45; text-transform: uppercase;
  }
  .bullet { color: var(--brand-blue); margin: 0 8px; }
  .bullet:first-child { margin-left: 0; }
  .bullet-blank { visibility: hidden; }
</style>
</head>
<body>
<main class="canvas">

  <section class="card card-front" aria-label="Business card front">
    <svg class="card-wave" viewBox="0 0 910 520" aria-hidden="true">
      <path d="M0,345 C210,375 390,490 620,520 L0,520 Z" fill="var(--brand-green)"/>
      <path d="M0,355 C220,388 410,490 680,520" fill="none" stroke="var(--line-white)" stroke-width="4"/>
      <path d="M0,385 C230,418 420,495 590,520" fill="none" stroke="var(--line-white)" stroke-width="2"/>
    </svg>

    <div class="name-block">
      <p class="person-name">Your Name</p>
      <p class="person-role">Position</p>
    </div>
    <p class="address">123 B. XYZ, Suite 000<br>MNOPQT, PK 9999</p>
    <ul class="contact-list">
      <li>
        <svg class="contact-icon" viewBox="0 0 16 16" aria-hidden="true"><path d="M3 1l3 3-2 2c1 2 3 4 5 5l2-2 3 3-2 2C7 14 2 9 1 3z" fill="var(--brand-green)"/></svg>
        555 010 2048
      </li>
      <li>
        <svg class="contact-icon" viewBox="0 0 16 16" aria-hidden="true"><rect x="1" y="3" width="14" height="10" fill="var(--brand-green)"/><path d="M1 3l7 6 7-6" fill="none" stroke="#fff" stroke-width="1.5"/></svg>
        hello@brightnestclean.net
      </li>
      <li>
        <svg class="contact-icon" viewBox="0 0 16 16" aria-hidden="true"><circle cx="8" cy="8" r="7" fill="var(--brand-green)"/><path d="M1 8h14M8 1v14" stroke="#fff" stroke-width="1.2"/></svg>
        brightnestclean.net
      </li>
    </ul>

    <div class="brand-mark">
      <span class="brand-dot" aria-hidden="true"></span>
      <span>Bright Nest<span class="brand-sub">CLEANING SERVICE</span></span>
    </div>
  </section>

  <section class="card card-back" aria-label="Business card back">
    <svg class="card-wave" viewBox="0 0 910 520" aria-hidden="true">
      <path d="M0,305 C260,325 520,440 910,455 L910,520 L0,520 Z" fill="var(--brand-blue)"/>
      <path d="M0,320 C270,342 540,452 910,475" fill="none" stroke="var(--card-black)" stroke-width="4"/>
    </svg>

    <div class="brand-mark">
      <span class="brand-dot" aria-hidden="true"></span>
      <span>Bright Nest<span class="brand-sub">CLEANING SERVICE</span></span>
    </div>

    <ul class="service-list">
      <li><span class="bullet">✦</span>Pressure cleaning<span class="bullet">✦</span>Window cleaning<span class="bullet">✦</span>Office</li>
      <li><span class="bullet">✦</span>End of lease clean<span class="bullet">✦</span>Accommodation</li>
      <li><span class="bullet">✦</span>Industrial and commercial cleaning</li>
      <li><span class="bullet bullet-blank" aria-hidden="true">✦</span>And house cleaning</li>
    </ul>
  </section>

</main>
</body>
</html>
```